Owner
Vireltex Golf Cart Cushion Covers
Bright & Fun-filled
Maelys Brant
348 Heron Mill Lane
Stamford, CT
maelysbrant@snugwraps.example
snugwraps.example
Snug Wraps are golf cart cushion covers made out of Vireltex Fleece. They are made in the USA.
Vireltex fleece golf cart cushion covers
available with custom embroidery

```html
<!DOCTYPE html>
<html lang="en">
<head>
<meta charset="utf-8">
<title>Snug Wraps Stationery</title>
<link rel="stylesheet" href="https://fonts.googleapis.com/css2?family=Open+Sans:wght@400;700&display=swap">
<style>
:root{
  --bg:#e7e3de;
  --paper:#ffffff;
  --ink:#333333;
  --muted:#8a8a8a;
  --rule:#9a9a9a;
  --accent:#e0197d;
  --faint:#eeeeee;
  --black:#141414;
  --shadow:0 2px 6px rgba(0,0,0,.18);
}
*{box-sizing:border-box;margin:0;padding:0}
html,body{width:1200px;height:566px;overflow:hidden}
body{background:var(--bg);font-family:"Open Sans",Arial,sans-serif;color:var(--ink);position:relative}
.sheet,.envelope,.card{position:absolute;background:var(--paper);box-shadow:var(--shadow)}
.brand{display:flex;align-items:center;gap:4px;font-weight:700;color:var(--ink);white-space:nowrap}
.brand-dot{width:.8em;height:.8em;border-radius:50%;background:var(--accent);flex:none}
.tagline{font-size:4px;color:var(--muted);line-height:1.3}
.contact{position:absolute;font-size:4px;line-height:1.4;color:var(--muted);text-align:right}
.watermark{position:absolute;font-weight:700;color:var(--faint);white-space:nowrap}

.letterhead{left:34px;top:65px;width:334px;height:441px}
.letterhead .brand{position:absolute;left:14px;top:16px;font-size:15px}
.letterhead .tagline{position:absolute;left:14px;top:38px;width:90px}
.letterhead .contact{right:12px;top:14px}
.letterhead .watermark{left:70px;top:225px;font-size:44px}

.fax{left:391px;top:65px;width:336px;height:441px}
.fax .brand{position:absolute;left:14px;top:16px;font-size:15px}
.fax .tagline{position:absolute;left:14px;top:38px;width:90px}
.fax .contact{right:12px;top:14px}
.fax-title{position:absolute;left:20px;top:136px;font-size:16px;font-weight:700}
.fax-fields{position:absolute;left:20px;top:172px;width:296px;display:grid;grid-template-columns:1fr 1fr;column-gap:10px;row-gap:6px}
.field{font-size:5px;border-bottom:1px solid var(--rule);padding-bottom:2px}
.fax-checks{position:absolute;left:20px;top:246px;display:flex;gap:14px}
.check{display:flex;align-items:center;gap:4px;font-size:5px}
.check i{width:7px;height:7px;border:1px solid var(--rule);display:block}

.envelope{width:413px;height:120px}
.env-back{left:763px;top:58px;overflow:hidden}
.env-back svg{position:absolute;inset:0}
.env-back .brand{position:absolute;left:50%;top:40px;transform:translateX(-50%);font-size:10px;color:var(--ink)}
.env-mid{left:763px;top:120px}
.env-front{left:763px;top:172px;height:165px}
.env-front .brand{position:absolute;left:14px;top:14px;font-size:13px}
.env-front .tagline{position:absolute;left:14px;top:34px;width:80px}
.env-front .site{position:absolute;left:14px;bottom:10px;font-size:4px;color:var(--muted)}
.env-front .watermark{right:14px;top:70px;font-size:30px}
.env-mid .watermark{right:14px;top:40px;font-size:30px}

.card{width:125px;height:72px}
.card-front{left:775px;top:360px}
.card-front .brand{position:absolute;left:8px;top:10px;font-size:10px}
.card-front .tagline{position:absolute;left:8px;top:28px;width:60px;font-size:3.5px}
.card-back{left:912px;top:360px}
.card-back .brand{position:absolute;left:8px;top:22px;font-size:10px}
.card-back .person{position:absolute;right:7px;top:8px;text-align:right;font-size:5px;font-weight:700}
.card-back .person span{display:block;font-weight:400;color:var(--muted);font-size:4px}
.card-back .contact{right:7px;bottom:8px;font-size:3.5px}
.card-dark{left:775px;top:456px;background:var(--black)}
.card-dark .brand{position:absolute;left:8px;top:12px;font-size:10px;color:#fff}
.card-dark .tagline{position:absolute;left:8px;top:30px;width:60px;font-size:3.5px;color:#aaa}
</style>
</head>
<body>

<section class="sheet letterhead">
  <div class="brand"><span class="brand-dot"></span>Snug Wraps</div>
  <p class="tagline">Vireltex fleece golf cart cushion covers</p>
  <p class="contact">348 Heron Mill Lane<br>Stamford, CT<br>maelysbrant@snugwraps.example<br>snugwraps.example</p>
  <div class="watermark">Snug Wraps</div>
</section>

<section class="sheet fax">
  <div class="brand"><span class="brand-dot"></span>Snug Wraps</div>
  <p class="tagline">Vireltex fleece golf cart cushion covers</p>
  <p class="contact">348 Heron Mill Lane<br>Stamford, CT<br>maelysbrant@snugwraps.example<br>snugwraps.example</p>
  <h1 class="fax-title">FAX</h1>
  <div class="fax-fields">
    <div class="field">To:</div><div class="field">From:</div>
    <div class="field">Fax:</div><div class="field">Pages:</div>
    <div class="field">Phone:</div><div class="field">Date:</div>
    <div class="field">Re:</div><div class="field">CC:</div>
  </div>
  <div class="fax-checks">
    <span class="check"><i></i>Urgent</span>
    <span class="check"><i></i>For Review</span>
    <span class="check"><i></i>Please Comment</span>
    <span class="check"><i></i>Please Reply</span>
    <span class="check"><i></i>Please Recycle</span>
  </div>
</section>

<section class="envelope env-back">
  <svg width="413" height="120" viewBox="0 0 413 120" aria-hidden="true">
    <polygon points="0,0 413,0 206,78" fill="#141414"/>
  </svg>
  <div class="brand" style="color:#fff"><span class="brand-dot"></span>Snug Wraps</div>
</section>

<section class="envelope env-mid">
  <div class="watermark">Snug Wraps</div>
</section>

<section class="envelope env-front">
  <div class="brand"><span class="brand-dot"></span>Snug Wraps</div>
  <p class="tagline">348 Heron Mill Lane<br>Stamford, CT</p>
  <p class="site">snugwraps.example</p>
  <div class="watermark">Snug Wraps</div>
</section>

<section class="card card-front">
  <div class="brand"><span class="brand-dot"></span>Snug Wraps</div>
  <p class="tagline">Vireltex fleece golf cart cushion covers</p>
</section>

<section class="card card-back">
  <p class="person">Maelys Brant<span>Owner</span></p>
  <div class="brand"><span class="brand-dot"></span>Snug Wraps</div>
  <p class="contact">348 Heron Mill Lane, Stamford, CT<br>maelysbrant@snugwraps.example<br>snugwraps.example</p>
</section>

<section class="card card-dark">
  <div class="brand"><span class="brand-dot"></span>Snug Wraps</div>
  <p class="tagline">available with custom embroidery</p>
</section>

</body>
</html>
```